New Digital Marketing Company Needs Web Design

Introduction

Brightcrest gives advice to small businesses about their websites and digital marketing strategies and builds working relationships with clients to understand their business and maximise its online presence.

Brightcrest offers services to support its clients needs such as: website auditing & search engine optimisation (SEO), Quorvo Promoline, Chatterlane Advertising, newsletter development & management, online performance reporting, email setup & management, website hosting, maintenance & backup, web development, web updates & web design.

Design Specification

The site should have a clean & professional look and use the colour scheme from the logo (attached below).

The design should consist of 2 templates; The homepage & content page.

Homepage Design

The homepage should have a header with logo, contact number and email and menu. Followed underneath by a slider and then individual blocks for key services. Under the key services should be a testimonial block with 3 testimonials. Finally the footer with company details, menu links and location map.

Header Info:

Contact number: 01632 960481
Email: info@brightcrest-demo.co.uk

Menu: Home Services About Contact

Slider Design:

The slider should be full page and show an image with text.

Key Services:

The key services should have a relevant icon and brief description.

The key services are:

Digital Marketing

Website Hosting & Management

Website Health Check (SEO)

Website Updating & Development

Newsletter Management

Email Management

Note: Lorem Ipsum can be used for brief description...

Testimonials:

There should be 3 testimonials side by side and they should include a headshot image of the person giving the testimonial.

Note: Lorem Ipsum and sample images can be used for testimonials...

Footer:

The footer should have 3 sections:

Menu links:

Digital Marketing About
Quorvo Promoline Contact
Chatterlane Advertising Privacy Policy
Search Engine Optimisation (SEO) Terms & Conditions
Website Hosting FAQ
Newsletter Management

Company Information:

BrightCrest
14 Marlow Close
Bracknell
Berskhire
ZZ9 4QT
Tel: 01632 960481

Chatterlane icon - Pipwave icon - Careernest icon

Location

Quorvo map

Footer Bottom:

Copyright message.

Content Design

The content design should have the common header and footer.

Each content page should have a banner for image with text description (page title).

The content page should have area for text description and area for a video display if available.

There should be a right column (possibly) for modules (latest blog, latest Chatterlane feeds, testimonial)

Project Deadline Extended
Reason: I have had to extend the deadline as could not review while on vacation and need to feedback to some designers for content page design. Many thanks for your understanding.

Target Market(s)

Industry/Entity Type

Digital

Number of Pages Required

2 page

Requirements
Must have
• The site should have a clean & professional look and use the colour scheme from the logo (attached below).
• The design should consist of 2 templates; The homepage & content page.

```html
<!DOCTYPE html>
<html lang="en">
<head>
<meta charset="utf-8">
<title>BrightCrest – Home</title>
<link href="https://fonts.googleapis.com/css2?family=Lato:ital,wght@0,400;0,700;0,900;1,400&family=Oswald:wght@400;500&display=swap" rel="stylesheet">
<style>
:root{
  --plum:#6b1a4f;
  --indigo:#463f67;
  --ink:#222;
  --body:#333;
  --grey-bg:#eeeeee;
  --icon-dark:#2b2b2b;
  --footer:#1d1f27;
  --footer-line:#3a3c46;
  --white:#fff;
}
*{box-sizing:border-box;margin:0;padding:0}
html,body{width:1200px;height:2703px;overflow:hidden}
body{position:relative;background:var(--white);font-family:"Lato",sans-serif;color:var(--body)}
.abs{position:absolute}

/* header */
.site-header{left:0;top:0;width:1200px;height:120px;background:linear-gradient(#fff,#f2f2f2)}
.brand{left:80px;top:20px;display:flex;align-items:center;gap:12px}
.brand-dot{width:52px;height:52px;border-radius:50%;background:var(--indigo)}
.brand-name{font-size:46px;font-weight:900;color:var(--plum);line-height:1}
.brand-tag{left:150px;top:80px;font-size:15px;letter-spacing:2.4px;color:var(--indigo);font-weight:700}
.contact-item{top:16px;display:flex;gap:10px;align-items:flex-start}
.contact-item svg{width:34px;height:50px}
.contact-item p{font-size:13px;font-weight:700;color:var(--ink);line-height:1.5;padding-top:2px}
.main-nav{top:78px;left:670px;display:flex;gap:0}
.main-nav a{font-size:17px;font-weight:700;color:var(--ink);text-decoration:none;width:115px;display:block}
.main-nav a.current{color:var(--indigo)}

/* slider */
.hero{left:0;top:120px;width:1200px;height:483px;background:radial-gradient(ellipse at 55% 45%,#ffffff 0%,#bfe6fb 28%,#2b8fd0 58%,#0b2f5a 100%)}
.hero-title{left:0;top:180px;width:1200px;text-align:center;font-family:"Oswald",sans-serif;font-size:84px;font-weight:500;color:#111;transform:scaleX(.85);letter-spacing:-1px}
.hero-caption{left:0;top:420px;width:1200px;height:63px;background:rgba(10,20,40,.45);color:#fff;font-family:"Oswald",sans-serif;font-size:28px;padding:10px 0 0 85px}
.hero-arrow{top:218px;width:30px;height:42px;background:rgba(90,90,90,.75)}

/* about */
.about-head{left:82px;top:640px;display:flex;align-items:baseline;gap:10px;width:662px;border-bottom:1px solid #ccc;padding-bottom:10px}
.about-head .dot{width:22px;height:22px;border-radius:50%;background:var(--indigo);align-self:center}
.about-head h2{font-size:34px;font-weight:900;color:var(--ink)}
.about-head h2 span{color:var(--plum)}
.about-head small{font-size:10px;letter-spacing:1.5px;color:#555;margin-left:6px}
.about-rule{left:82px;top:697px;width:60px;height:3px;background:var(--plum)}
.about-text{left:82px;top:712px;width:664px;font-size:14.4px;line-height:25.8px;text-align:justify;color:var(--ink)}
.btn-more{left:82px;top:990px;width:135px;height:40px;border-radius:20px;background:var(--plum);color:#fff;font-size:14px;font-weight:700;padding:11px 0 0 16px}
.btn-more i{position:absolute;right:8px;top:8px;width:24px;height:24px;border-radius:50%;background:#8c8c8c}

/* inquiry */
.inquiry{left:790px;top:650px;width:330px;height:385px;border:1px solid #d6d6d6;background:#fff}
.inquiry-head{left:-1px;top:-1px;width:330px;height:85px}
.inquiry-head span{position:absolute;left:0;top:12px;width:100%;text-align:center;color:#fff;font-size:26px;font-weight:700}
.field{left:18px;width:294px;height:40px;border:1px solid #ccc;border-radius:3px;font-size:13px;color:#333;padding:11px 10px}
.btn-submit{left:18px;top:322px;width:294px;height:38px;background:var(--indigo);color:#fff;font-size:19px;font-weight:700;text-align:center;padding-top:7px;border-radius:2px}

/* services */
.services{left:0;top:1080px;width:1200px;height:755px;background:var(--grey-bg)}
.section-title{width:1200px;left:0;text-align:center;font-size:33px;font-weight:700;color:var(--plum)}
.section-rule{left:465px;width:270px;height:1px;background:#bbb}
.section-rule::after{content:"";position:absolute;left:100px;top:-1px;width:70px;height:3px;background:var(--plum)}
.service{width:360px;text-align:center}
.service-icon{width:152px;height:152px;margin:0 auto;border-radius:50%;border:2px solid #999;padding:6px;background:#fff}
.service-icon div{width:100%;height:100%;border-radius:50%;background:var(--icon-dark);display:flex;align-items:center;justify-content:center}
.service-icon.active div{background:var(--plum)}
.service h3{margin-top:30px;font-size:19.5px;font-weight:700;color:var(--plum)}
.service p{margin-top:12px;font-size:13px;line-height:20px;color:var(--ink)}
.service p b{color:var(--indigo);font-weight:400}

/* testimonials */
.person{width:180px;text-align:center}
.photo{width:114px;height:114px;margin:0 auto;border-radius:50%;border:4px solid #9a9a9a}
.photo.active{border-color:var(--plum)}
.person p{margin-top:14px;font-size:14px;font-weight:700;color:var(--ink)}
.person.active p{color:var(--plum)}
.t-arrow{top:2010px;width:16px;height:30px}
.quote-box{left:80px;top:2155px;width:1040px;height:138px;border:1px solid #d4d4d4;background:#fff;padding:24px 30px;text-align:center;font-style:italic;font-size:13px;line-height:27px;color:#444}
.notch{left:262px;top:2142px;width:24px;height:24px;background:#fff;border-left:1px solid #d4d4d4;border-top:1px solid #d4d4d4;transform:rotate(45deg)}
.qmark{color:#bbb;font-size:36px;font-style:normal;font-family:Georgia,serif;vertical-align:-12px}

/* newsletter */
.newsletter{left:0;top:2346px;width:1200px;height:91px;background:var(--plum)}
.newsletter h3{position:absolute;left:140px;top:24px;color:#fff;font-size:30px;font-weight:700}
.nl-input{left:478px;top:25px;width:470px;height:40px;background:#fff;font-size:12px;color:#666;padding:13px 12px}
.nl-btn{left:960px;top:25px;width:160px;height:40px;border:2px solid #fff;background:var(--indigo);color:#fff;font-size:17px;font-weight:700;text-align:center;padding-top:8px}

/* footer */
.site-footer{left:0;top:2437px;width:1200px;height:213px;background:var(--footer);color:#e6e6e6}
.f-head{font-size:16px;font-weight:700;color:#fff;padding-bottom:12px;border-bottom:1px solid var(--footer-line)}
.f-links{font-size:12.5px;line-height:33px}
.f-links li{list-style:none}
.f-links li::before{content:"• "}
.f-contact{font-size:13px;line-height:19px}
.map{width:255px;height:114px;background:linear-gradient(135deg,#e9e4d6,#cfdcc2 55%,#e3d9c8)}
.bottom-bar{left:0;top:2650px;width:1200px;height:53px;background:var(--indigo);color:#fff;font-size:13px;font-weight:700;padding:17px 0 0 82px}
.social{top:2662px;width:30px;height:30px;border-radius:50%;background:#1e9ad6;border:2px solid #fff}
</style>
</head>
<body>

<header class="site-header abs">
  <div class="brand abs"><span class="brand-dot"></span><span class="brand-name">BrightCrest</span></div>
  <div class="brand-tag abs">GROWING YOUR BUSINESS ONLINE</div>

  <div class="contact-item abs" style="left:775px">
    <svg viewBox="0 0 34 50"><path d="M17 48c-3-8-15-16-15-30a15 15 0 0 1 30 0c0 14-12 22-15 30z" fill="var(--plum)"/><rect x="9" y="12" width="16" height="11" fill="#fff"/><path d="M9 12l8 6 8-6" stroke="var(--plum)" stroke-width="1.5" fill="none"/></svg>
    <p>Mail Us<br>info@brightcrest-demo.co.uk</p>
  </div>
  <div class="contact-item abs" style="left:990px">
    <svg viewBox="0 0 34 50"><path d="M17 48c-3-8-15-16-15-30a15 15 0 0 1 30 0c0 14-12 22-15 30z" fill="var(--plum)"/><path d="M11 10c2 0 3 3 2 4l-1 1c1 3 3 5 6 6l1-1c1-1 4 0 4 2s-2 3-4 3c-6 0-11-5-11-11 0-2 1-4 3-4z" fill="#fff"/></svg>
    <p>Call Us Now!<br>01632 960481</p>
  </div>

  <nav class="main-nav abs">
    <a href="#" class="current">Home</a>
    <a href="#">Services</a>
    <a href="#">About Us</a>
    <a href="#">Contact Us</a>
  </nav>
</header>

<section class="hero abs" role="img" aria-label="Slider photograph: tunnel of glowing blue binary digits">
  <div class="hero-title abs">DIGITAL MARKETING</div>
  <div class="hero-caption abs">We Work With Our Clients To Understand Their Business And Maximise Their Online Presence.</div>
  <div class="hero-arrow abs" style="left:0"><svg width="30" height="42"><path d="M18 14l-7 7 7 7" stroke="#fff" stroke-width="3" fill="none"/></svg></div>
  <div class="hero-arrow abs" style="left:1170px"><svg width="30" height="42"><path d="M12 14l7 7-7 7" stroke="#fff" stroke-width="3" fill="none"/></svg></div>
</section>

<div class="about-head abs"><span class="dot"></span><h2>About <span>BrightCrest</span></h2><small>GROWING YOUR BUSINESS ONLINE</small></div>
<div class="about-rule abs"></div>
<p class="about-text abs">Lorem ipsum dolor sit amet, consectetuer adipiscing elit, sed diam nonummy nibh euismod tincidunt ut laoreet dolore magna aliquam erat volutpat. Ut wisi enim ad minim veniam, quis nostrud exerci tation ullamcorper suscipit lobortis nisl ut aliquip ex ea commodo consequat. Duis autem vel eum iriure dolor in hendrerit in vulputate velit esse molestie consequat, vel illum dolore eu feugiat nulla facilisis at vero eros et accumsan et iusto odio dignissim qui blandit praesent luptatum zzril delenit augue duis dolore te feugait nulla facilisi.Lorem ipsum dolor sit amet, consectetuer adipiscing elit, sed diam nonummy nibh euismod tincidunt ut laoreet dolore magna aliquam erat volutpat. Ut wisi enim ad minim veniam, quis nostrud exerci tation ullamcorper suscipit lobortis nisl ut aliquip ex ea commodo consequat. Duis autem vel eum iriure dolor in hendrerit in vulputate velit esse molestie.</p>
<div class="btn-more abs">Read More<i><svg width="24" height="24"><path d="M10 7l5 5-5 5" stroke="#fff" stroke-width="2" fill="none"/></svg></i></div>

<aside class="inquiry abs">
  <svg class="inquiry-head abs" viewBox="0 0 330 85"><path d="M0 0H330V50L165 82L0 50Z" fill="var(--indigo)"/><path d="M0 50L165 82L330 50" stroke="var(--plum)" stroke-width="4" fill="none"/></svg>
  <div class="inquiry-head abs"><span>Quick Inquiry</span></div>
  <div class="field abs" style="top:102px">Name</div>
  <div class="field abs" style="top:150px">Email</div>
  <div class="field abs" style="top:197px">Phone</div>
  <div class="field abs" style="top:244px;height:66px">Message</div>
  <div class="btn-submit abs">Submit</div>
</aside>

<section class="services abs">
  <h2 class="section-title abs" style="top:50px">Our Services</h2>
  <div class="section-rule abs" style="top:108px"></div>

  <div class="service abs" style="left:57px;top:165px">
    <div class="service-icon active"><div><svg width="64" height="64" viewBox="0 0 64 64"><rect x="14" y="8" width="22" height="44" rx="4" fill="#fff"/><rect x="18" y="14" width="14" height="30" fill="var(--plum)"/><path d="M20 26h6l6-5v14l-6-5h-6z" fill="#fff"/><path d="M42 22l8-4M43 29h9M42 36l8 4" stroke="#fff" stroke-width="3"/></svg></div></div>
    <h3>Digital Marketing</h3>
    <p>Lorem ipsum dolor sit amet, consectet<br>adipiscing elit, sed diam...<b>[+]</b></p>
  </div>
  <div class="service abs" style="left:420px;top:165px">
    <div class="service-icon"><div><svg width="64" height="64" viewBox="0 0 64 64"><path d="M18 30a9 9 0 0 1 4-17 12 12 0 0 1 22 2 8 8 0 0 1 2 15z" fill="#fff"/><rect x="14" y="32" width="36" height="18" rx="2" fill="none" stroke="#fff" stroke-width="3"/><path d="M8 52h48" stroke="#fff" stroke-width="4"/><path d="M30 38l6 6-3 0 2 3" stroke="#fff" stroke-width="2" fill="none"/></svg></div></div>
    <h3>Website Hosting &amp; Management</h3>
    <p>Lorem ipsum dolor sit amet, consectet<br>adipiscing elit, sed diam...<b>[+]</b></p>
  </div>
  <div class="service abs" style="left:785px;top:165px">
    <div class="service-icon"><div><svg width="64" height="64" viewBox="0 0 64 64"><circle cx="36" cy="36" r="10" fill="none" stroke="#fff" stroke-width="4"/><path d="M43 43l12 12" stroke="#fff" stroke-width="6"/><path d="M12 16l12 12M10 22l6-6-4-4" stroke="#fff" stroke-width="5" fill="none"/></svg></div></div>
    <h3>Website Health Check (SEO)</h3>
    <p>Lorem ipsum dolor sit amet, consectet<br>adipiscing elit, sed diam...<b>[+]</b></p>
  </div>

  <div class="service abs" style="left:57px;top:452px">
    <div class="service-icon"><div><svg width="64" height="64" viewBox="0 0 64 64"><rect x="10" y="14" width="44" height="36" rx="3" fill="none" stroke="#fff" stroke-width="3"/><path d="M10 22h44" stroke="#fff" stroke-width="3"/><path d="M25 30l-6 6 6 6M39 30l6 6-6 6M34 28l-4 16" stroke="#fff" stroke-width="2.5" fill="none"/></svg></div></div>
    <h3>Website Updating &amp; Development</h3>
    <p>Lorem ipsum dolor sit amet, consectet<br>adipiscing elit, sed diam...<b>[+]</b></p>
  </div>
  <div class="service abs" style="left:420px;top:452px">
    <div class="service-icon"><div><svg width="64" height="64" viewBox="0 0 64 64"><circle cx="26" cy="22" r="9" fill="#fff"/><path d="M10 50c0-10 7-16 16-16s12 4 13 8v8z" fill="#fff"/><rect x="34" y="36" width="24" height="16" fill="#fff" stroke="var(--icon-dark)" stroke-width="2"/><path d="M34 36l12 9 12-9" stroke="var(--icon-dark)" stroke-width="2" fill="none"/></svg></div></div>
    <h3>Newsletter Management</h3>
    <p>Lorem ipsum dolor sit amet, consectet<br>adipiscing elit, sed diam...<b>[+]</b></p>
  </div>
  <div class="service abs" style="left:785px;top:452px">
    <div class="service-icon"><div><svg width="64" height="64" viewBox="0 0 64 64"><circle cx="26" cy="22" r="9" fill="#fff"/><path d="M10 50c0-10 7-16 16-16s12 4 13 8v8z" fill="#fff"/><text x="36" y="54" font-family="Lato,sans-serif" font-size="24" font-weight="700" fill="#fff">@</text></svg></div></div>
    <h3>Email Management</h3>
    <p>Lorem ipsum dolor sit amet, consectet<br>adipiscing elit, sed diam...<b>[+]</b></p>
  </div>
</section>

<h2 class="section-title abs" style="top:1882px">Client Testimonials</h2>
<div class="section-rule abs" style="top:1940px;background:transparent"></div>

<svg class="t-arrow abs" style="left:168px" viewBox="0 0 16 30"><path d="M14 2L2 15l12 13" stroke="#ccc" stroke-width="2" fill="none"/></svg>
<svg class="t-arrow abs" style="left:1014px" viewBox="0 0 16 30"><path d="M2 2l12 13-12 13" stroke="#ccc" stroke-width="2" fill="none"/></svg>

<div class="person active abs" style="left:191px;top:1968px"><div class="photo active" role="img" aria-label="Headshot of client" style="background:linear-gradient(#8fd6d6,#e4b89a)"></div><p>Mr. Tarvin Oakley</p></div>
<div class="person abs" style="left:407px;top:1968px"><div class="photo" role="img" aria-label="Headshot of client" style="background:linear-gradient(#d0d0d0,#5a4a40)"></div><p>Mrs. Lenna Varsk</p></div>
<div class="person abs" style="left:614px;top:1968px"><div class="photo" role="img" aria-label="Headshot of client" style="background:linear-gradient(#bdbdbd,#2b2b2b)"></div><p>Mr. Dorian Pell</p></div>
<div class="person abs" style="left:827px;top:1968px"><div class="photo" role="img" aria-label="Headshot of client" style="background:linear-gradient(#d8d8d8,#3a3f4a)"></div><p>Mr. Aldo Rensky</p></div>

<div class="quote-box abs"><span class="qmark">&ldquo;</span> Lorem ipsum dolor sitamet, consectetuer adipiscing sed diam nonummy nibh euismod tincidunt ut laoreet dolore magna alqua volutpat. Ut wisi enim ad minim veniam, quis nostrud exerci tation ullamcorper suscipit lobortis nisl ut aliquip ex ea commodo consequat. Duis autem vel eum iriure dolor in hendrerit in vulputate velit esse molestie consequat.ud exerci tation ullamcorper suscipit lobortis nisl ut aliquip ex ea commodo. <span class="qmark">&rdquo;</span></div>
<div class="notch abs"></div>

<section class="newsletter abs">
  <svg class="abs" style="left:80px;top:22px" width="46" height="46" viewBox="0 0 46 46"><circle cx="23" cy="23" r="21" fill="none" stroke="#fff" stroke-width="2"/><circle cx="23" cy="23" r="16" fill="#fff"/><rect x="14" y="17" width="18" height="12" fill="var(--plum)"/><path d="M14 17l9 7 9-7" stroke="#fff" stroke-width="1.5" fill="none"/></svg>
  <h3>Newsletter Signup</h3>
  <svg class="abs" style="left:420px;top:18px" width="30" height="55"><path d="M4 3l22 24L4 52" stroke="#fff" stroke-width="2" fill="none"/></svg>
  <div class="nl-input abs">Email</div>
  <div class="nl-btn abs">SUBSCRIBE</div>
</section>

<footer class="site-footer abs">
  <div class="abs" style="left:82px;top:24px;width:355px">
    <div class="f-head">QUICK LINKS</div>
    <ul class="f-links abs" style="left:0;top:46px;width:200px">
      <li>Digital Marketing</li><li>Quorvo Promoline</li><li>Chatterlane Advertising</li><li>Search Engine Optimisation</li>
    </ul>
    <ul class="f-links abs" style="left:213px;top:46px;width:160px">
      <li>Website Hosting&nbsp; FAQ</li><li>Newsletter Management</li><li>About Us</li><li>Contact Us</li>
    </ul>
  </div>
  <div class="abs" style="left:560px;top:24px;width:245px">
    <div class="f-head">CONTACT DETAILS</div>
    <svg class="abs" style="left:2px;top:50px" width="14" height="18"><path d="M7 17C5 12 1 9 1 6a6 6 0 0 1 12 0c0 3-4 6-6 11z" fill="#ddd"/><circle cx="7" cy="6" r="2" fill="var(--footer)"/></svg>
    <p class="f-contact abs" style="left:24px;top:48px;width:200px"><b>Brightcrest</b><br>16 Lorem ipsum dolor sit&nbsp; sed benetion, Street no-123456</p>
    <svg class="abs" style="left:2px;top:118px" width="14" height="14"><path d="M3 1c2 0 3 3 2 4l-1 1c1 2 2 3 4 4l1-1c1-1 4 0 4 2s-1 2-3 2C5 13 1 9 1 4c0-2 1-3 2-3z" fill="#ddd"/></svg>
    <p class="f-contact abs" style="left:24px;top:115px">01632 960481</p>
    <svg class="abs" style="left:2px;top:151px" width="14" height="10"><rect width="14" height="10" fill="#ddd"/><path d="M0 0l7 5 7-5" stroke="var(--footer)" fill="none"/></svg>
    <p class="f-contact abs" style="left:24px;top:146px">info@brightcrest-demo.co.uk</p>
  </div>
  <div class="abs" style="left:865px;top:24px;width:255px">
    <div class="f-head">LOCATION MAP</div>
    <div class="map abs" style="left:0;top:47px" role="img" aria-label="Street map showing the office location"></div>
  </div>
</footer>

<div class="bottom-bar abs">Copyright © 2016 Brightcrest &nbsp;|&nbsp; All Rights Reserved &nbsp;|&nbsp; Privacy Policy &nbsp;|&nbsp; Terms &amp; Conditions</div>
<div class="social abs" style="left:1004px"></div>
<div class="social abs" style="left:1044px"></div>
<div class="social abs" style="left:1084px"></div>

</body>
</html>
```